Banner Ad Design Project

I need a banner design. The website is under construction at www.brightmarrow.example

Name: Bright Marrow
Tagline: Steady Sparks for crowded calendars

This is a leadership development and executive coaching site. The past site is live at www.quillstepnow.example. (so you can get a sense of the content)

The audience are (BUSY) executives, senior managers, leaders and top professionals, so the feel needs to be highly professional but also modern and fresh. I want to communicate energy but also solid and trust worthy and not too new agey. The audience are also people with strong social values who want to change things - so not too corporate (Ie suits!)

I would like the design to be floating on a white background, very clean and simple. I am attracted to reds or sunset (burn orange crimson colors.) But totally open to any color ideas.
I am giving an open brief for your ideas.
Here are the dimensions 960px wide, roughly 190px height.

Reason: The weekend might give more time to designers to get involved. Thanks Vina

Hi designers

You may not have seen the additions I gave to this brief.

The banner should not have leader out front photo's. Maybe less corporate than I initially thought. 
Not too corporate (no suits!) Please no chess pieces, jigsaw pieces, cartoon images, cliche leadership images. 
Am am trying for inspiration /inspiring whilst still being professional. Very simple and clean.
Please can the design be floating in a white background so that the web page is borderless - A bit like it is in http://palmoriskel.example/
Thank you

Target Market(s)

Senior managers, executives but people who also want to change the world!

Industry/Entity Type

Construction

Requirements
Should not have
• Should not have leader out front photo's.
Maybe less corporate than I initially thought.
Am am trying for inspiration /inspiring whilst still being professional.
Please no chess pieces, jigsaw pieces, cartoon images, cliche leadership images. Not too corporate (Ie suits!)

Thanks

```html
<!DOCTYPE html>
<html lang="en">
<head>
<meta charset="utf-8">
<title>Bright Marrow – Steady Sparks for crowded calendars</title>
<link rel="stylesheet" href="https://fonts.googleapis.com/css2?family=Cormorant+Garamond:wght@500&display=swap">
<style>
  :root {
    --brand-red: #d8202a;
    --bg-light: #f2f2f2;
    --bg-mid: #e6e6e6;
    --visual-light: #fafafa;
    --visual-mid: #d9d9d9;
    --visual-accent: #b11d22;
  }
  html, body {
    margin: 0;
    padding: 0;
    overflow: hidden;
    background: #ffffff;
  }
  .banner {
    position: relative;
    width: 1200px;
    height: 238px;
    overflow: hidden;
    background: linear-gradient(90deg, var(--bg-mid) 0%, var(--bg-light) 45%, #ffffff 60%);
    font-family: "Cormorant Garamond", "Georgia", serif;
    font-weight: 500;
    color: var(--brand-red);
  }
  .brand-name {
    position: absolute;
    left: 48px;
    top: 58px;
    margin: 0;
    font-size: 76px;
    font-weight: 500;
    line-height: 1;
    white-space: nowrap;
  }
  .tagline {
    position: absolute;
    left: 52px;
    top: 156px;
    margin: 0;
    font-size: 24px;
    font-weight: 500;
    line-height: 1;
    white-space: nowrap;
  }
  .feature-visual {
    position: absolute;
    left: 600px;
    top: 0;
    width: 600px;
    height: 238px;
    background:
      radial-gradient(ellipse 90px 70px at 430px 150px, var(--visual-accent) 0%, rgba(177,29,34,0.6) 55%, rgba(177,29,34,0) 100%),
      linear-gradient(160deg, var(--visual-light) 0%, var(--visual-mid) 55%, var(--visual-light) 100%);
  }
</style>
</head>
<body>
  <header class="banner">
    <h1 class="brand-name">Bright Marrow</h1>
    <p class="tagline">Steady sparks for crowded calendars</p>
    <div class="feature-visual" role="img" aria-label="Photograph of scattered white puzzle pieces on a white surface with a single red piece standing out"></div>
  </header>
</body>
</html>
```